AUSTRALIAN CONSULTING FIRM BUSINESS CARD - MODERN

We are wanting a modern, clean lined business card design. We are professional niche consultancy firm situated in Australia called Marlow Advisory Partners Pty Ltd.
The card should communicate professionalism and creativity and draw on our logo design (attached).
The design should be two sided, landscape orientation.
Target Market(s)
government, not for profit sector, corporate clients
Industry/Entity Type
Landscape
Requirements
Must have
- logo
no new introduced colours

```html
<!DOCTYPE html>
<html lang="en">
<head>
<meta charset="utf-8">
<title>Marlow Advisory Partners – Business Card</title>
<link rel="stylesheet" href="https://fonts.googleapis.com/css2?family=Jost:wght@400;600;700&display=swap">
<style>
  :root {
    --charcoal: #2f2f2f;
    --paper: #ffffff;
    --green: #8dc63f;
    --magenta: #c05bb0;
    --sky: #1aa9e8;
    --navy: #1f3f9a;
    --backdrop: #eeeeee;
    --ink: #222222;
  }
  * { margin: 0; padding: 0; box-sizing: border-box; }
  html, body {
    width: 1200px; height: 686px; overflow: hidden;
    background: var(--backdrop);
    font-family: "Jost", "Helvetica Neue", Arial, sans-serif;
  }
  .sheet {
    position: relative; width: 1200px; height: 686px;
    display: flex; align-items: center; justify-content: center; gap: 32px;
  }
  .card {
    position: relative; width: 560px; height: 319px;
    border-radius: 14px; overflow: hidden;
    box-shadow: 0 6px 18px rgba(0,0,0,0.18);
  }
  .card-front { background: var(--paper); }
  .card-back { background: var(--charcoal); }

  .accent-field {
    position: absolute; top: 0; right: 0; height: 100%;
    background: linear-gradient(160deg, var(--magenta) 0%, var(--sky) 45%, var(--green) 100%);
  }
  .card-front .accent-field { width: 160px; }
  .card-back .accent-field { width: 26px; }

  /* front */
  .brand-lockup {
    position: absolute; left: 56px; top: 50%; transform: translateY(-50%);
    display: flex; align-items: center; gap: 14px;
  }
  .brand-dot {
    width: 40px; height: 40px; border-radius: 50%;
    background: var(--sky); flex: none;
  }
  .brand-name {
    color: var(--navy); font-weight: 700; font-size: 21px;
    line-height: 1.1; text-transform: uppercase; letter-spacing: 0.5px;
  }

  /* back */
  .back-mark {
    position: absolute; left: 0; top: 0; width: 164px; height: 100%;
    display: flex; flex-direction: column; align-items: center; justify-content: center; gap: 10px;
  }
  .back-mark .brand-dot { width: 34px; height: 34px; }
  .back-mark-name {
    color: var(--paper); font-weight: 600; font-size: 11px;
    text-align: center; line-height: 1.3; text-transform: uppercase; letter-spacing: 1px;
    width: 120px;
  }
  .info-panel {
    position: absolute; left: 164px; top: 22px; right: 46px; bottom: 22px;
    background: var(--paper);
  }
  .contact {
    position: absolute; left: 232px; top: 114px; color: var(--ink);
  }
  .contact-name {
    font-weight: 700; font-size: 15px; letter-spacing: 3px; margin-bottom: 18px;
  }
  .contact-line {
    font-size: 9.5px; letter-spacing: 1px; line-height: 1; margin-bottom: 10px;
  }
</style>
</head>
<body>
<main class="sheet">

  <section class="card card-front" aria-label="Card front">
    <div class="accent-field" role="img" aria-label="Decorative colour field in magenta, blue and green"></div>
    <div class="brand-lockup">
      <span class="brand-dot"></span>
      <span class="brand-name">Marlow Advisory<br>Partners Pty Ltd</span>
    </div>
  </section>

  <section class="card card-back" aria-label="Card back">
    <div class="info-panel"></div>
    <div class="accent-field" role="img" aria-label="Decorative colour strip in magenta, blue and green"></div>
    <div class="back-mark">
      <span class="brand-dot"></span>
      <span class="back-mark-name">Marlow Advisory Partners</span>
    </div>
    <div class="contact">
      <p class="contact-name">Corin Tallent</p>
      <p class="contact-line">Marlow Advisory Partners Pty Ltd. Australia</p>
      <p class="contact-line">corin.tallent@marlowadvisory.com.au</p>
      <p class="contact-line">+61 400 555 218</p>
    </div>
  </section>

</main>
</body>
</html>
```